A Spinner Of Grace Company Brochure

I am the owner of a Mobile Disc Jockey company specializing in weddings. I am looking for a Tri Fold color brochure that is modern and eye catching with the focus being on upscale wedding events. I also want it to be easy to read and not overly cluttered ! I would like it to reflect our website located at aspinnerofgrace.example
I also have different variations and file types of my logo such as jpeg and png files. I need some good dance floor pics. If you do not have any good stock photos I can look through my photo library. I uploaded a logo and pic I found from one of my videos. Not sure if it is worth anything.
We also do Uplighting and Photo Booths which I would like in the brochure. Much of the text copy needed can be taken from our website if needed. Please refer to the website to see what we do and our style.

Target Market(s)

upscale weddings

Industry/Entity Type

wedding dj entertainment & masters of ceremonies

Requirements
Nice to have
• nice pictures of packed dance floors and people having fun

```html
<!DOCTYPE html>
<html lang="en">
<head>
<meta charset="utf-8">
<title>A Spinner Of Grace – Tri-Fold Brochure, Inside Spread</title>
<link href="https://fonts.googleapis.com/css2?family=Arimo:wght@400;700&family=Fira+Sans+Condensed:wght@500;600;700&family=Open+Sans:wght@400&family=Parisienne&display=swap" rel="stylesheet">
<style>
  :root {
    --purple: #7b2f8b;
    --purple-text: #7a2f8a;
    --grey-text: #7d7d7d;
    --grey-bleed: #8a8b8c;
    --white: #ffffff;
    --ink: #111111;
    --canvas: #ffffff;
  }
  * { box-sizing: border-box; margin: 0; padding: 0; }
  html, body {
    width: 1200px; height: 881px; overflow: hidden; background: var(--canvas);
  }
  .stage {
    position: absolute; left: 0; top: 0;
    width: 1177px; height: 864px;
    transform: scale(1.0195, 1.0197); transform-origin: 0 0;
  }
  .panel-label {
    position: absolute; top: 16px; width: 240px; margin-left: -120px;
    text-align: center; font: 400 25px/1 "Open Sans", sans-serif; color: var(--ink);
  }
  .bleed {
    position: absolute; left: 105px; top: 57px; width: 936px; height: 766px;
    background: var(--grey-bleed); border: 1px solid #555;
  }
  .spread {
    position: absolute; left: 105px; top: 85px; width: 936px; height: 708px;
    background: var(--white); overflow: hidden;
  }
  .trim-line {
    position: absolute; left: 121px; top: 72px; width: 908px; height: 736px;
    border: 1px solid rgba(255,255,255,0.9); pointer-events: none;
  }
  .block { position: absolute; }
  .photo { position: absolute; }

  /* inside left */
  .photo--wedding {
    left: 0; top: 0; width: 312px; height: 252px;
    background: linear-gradient(160deg, #f4efe6 0%, #cfc4b2 35%, #8c8478 60%, #d8d2c8 100%);
  }
  .weddings-title {
    left: 22px; top: 262px; width: 280px; white-space: nowrap;
    font: 400 58px/1.4 "Parisienne", cursive; color: var(--purple-text);
    letter-spacing: 4px;
  }
  .weddings-tagline {
    left: 30px; top: 386px; width: 280px;
    font: 700 12.5px/15px "Arimo", sans-serif; color: var(--purple-text);
    letter-spacing: 0.5px; text-transform: uppercase;
  }
  .body-copy {
    font: 400 11.5px/14.3px "Arimo", sans-serif; text-align: justify;
    letter-spacing: 0.3px;
  }
  .body-copy p + p { margin-top: 14px; }
  .weddings-copy { left: 30px; top: 474px; width: 255px; color: var(--grey-text); }

  /* inside middle */
  .corporate {
    left: 312px; top: 0; width: 312px; height: 420px; background: var(--purple);
    color: var(--white); padding: 34px 28px 0 28px;
  }
  .corporate-title {
    font: 600 24px/1 "Fira Sans Condensed", sans-serif; text-align: center;
    margin: 0 -22px 14px; white-space: nowrap;
  }
  .corporate .body-copy { color: var(--white); }
  .corporate .phone-inline { font-size: 13.5px; }
  .photo--dancefloor {
    left: 312px; top: 420px; width: 312px; height: 187px;
    background: linear-gradient(120deg, #1a1030 0%, #7c3d8f 35%, #e3a7c9 55%, #3a3168 80%, #120c22 100%);
  }
  .brand {
    left: 312px; top: 607px; width: 312px; height: 101px;
    display: flex; align-items: center; justify-content: center; gap: 10px;
  }
  .brand-dot { width: 34px; height: 34px; border-radius: 50%; background: var(--purple); }
  .brand-name { font: 500 27px/1 "Fira Sans Condensed", sans-serif; color: var(--grey-text); }

  /* inside right */
  .feature {
    left: 624px; width: 312px; display: flex; align-items: flex-end; justify-content: center;
    padding-bottom: 6px;
    font: 700 36px/1 "Fira Sans Condensed", sans-serif; color: var(--white);
    letter-spacing: -0.5px;
  }
  .feature--booth {
    top: 0; height: 208px;
    background: linear-gradient(135deg, #0b1c24 0%, #1f6a72 40%, #6fb8b6 60%, #17323a 100%);
  }
  .feature--karaoke {
    top: 213px; height: 207px;
    background: linear-gradient(150deg, #3a6f9b 0%, #c9d6e4 30%, #e2b5a3 55%, #b0567d 80%, #36405a 100%);
  }
  .customers {
    left: 624px; top: 485px; width: 312px; text-align: center;
    font: 600 17.5px/22px "Fira Sans Condensed", sans-serif; color: var(--grey-text);
  }
  .customers strong { color: var(--purple-text); font-weight: 600; }
  .call-now {
    left: 624px; top: 607px; width: 312px; height: 101px; background: var(--purple);
    color: var(--white); text-align: center; padding-top: 21px;
    font: 400 24px/1 "Arimo", sans-serif; letter-spacing: 1.5px;
  }
  .call-now .call-number { display: block; margin-top: 11px; font-size: 31px; letter-spacing: 2px; }
</style>
</head>
<body>
<div class="stage">
  <div class="panel-label" style="left:234px">Inside Left</div>
  <div class="panel-label" style="left:542px">Inside Middle</div>
  <div class="panel-label" style="left:876px">Inside Right</div>

  <div class="bleed"></div>

  <div class="spread">
    <!-- inside left -->
    <div class="photo photo--wedding" role="img" aria-label="Photo of a bride and groom walking out of their ceremony while guests applaud"></div>
    <h1 class="block weddings-title">Weddings</h1>
    <p class="block weddings-tagline">Entertainment planning &amp;<br>coordination the way you want it</p>
    <div class="block body-copy weddings-copy">
      <p>Beginning with your initial consultation, we listen to you and respond with creative ideas and helpful advice so your event is all about you. We know it’s more than just great music, it’s keeping you guests engaged and coordinating with your venue and vendors for a smooth and timely event everyone will never forget.</p>
      <p>Contact us now and find out why so many couples continue to place their faith and trust in us to help them create the ultimate wedding experience.</p>
    </div>

    <!-- inside middle -->
    <section class="block corporate">
      <h2 class="corporate-title">Corporate DJ Entertainment</h2>
      <div class="body-copy">
        <p>With over 30+ years of experience providing DJ entertainment and lighting services for corporate events and company parties, we understand how important creating the right atmosphere and delivering quality entertainment is to the success of your event. So whether you’re planning a sales incentive meeting, awards presentation, beach party, holiday party or gala evening, let us help you create an event your employees will never forget.</p>
        <p>Our DJs are always ready to fill your dance floor so everyone can cut loose and enjoy a well-deserved break. If you would rather a more reserved approach, we can also provide a non-interactive style as well! name a few.</p>
        <p>Call us now at <span class="phone-inline">(555) 014-2290</span> and let us help you create your next successful corporate event or company party.</p>
      </div>
    </section>
    <div class="photo photo--dancefloor" role="img" aria-label="Motion-blurred photo of guests dancing on a packed dance floor under purple lights"></div>
    <div class="block brand">
      <span class="brand-dot"></span>
      <span class="brand-name">A Spinner Of Grace</span>
    </div>

    <!-- inside right -->
    <div class="block feature feature--booth" role="img" aria-label="Photo of friends posing at a ring-lit photo booth">Photo Booth</div>
    <div class="block feature feature--karaoke" role="img" aria-label="Photo of a group of friends singing karaoke together">Karaoke</div>
    <p class="block customers">Join Over <strong>1,000 Happy Customers</strong><br>that have enjoyed A Spinner Of Grace<br>Have your event be remembered<br>as being one of the greats!</p>
    <div class="block call-now">Call us now<span class="call-number">(555) 014-2290</span></div>
  </div>

  <div class="trim-line"></div>
</div>
</body>
</html>
```